Orbel Appraisals website redesign

I would like to refresh my existing website of www.orbelappraisals-demo.com with new graphics, look and feel, as well as updated structure and wording. Content and layout changes have been uploaded to this project Brief.

My existing website has a dark feel. I am now looking for a light and energetic feel. Financial Services is my industry, so the website should be reflect that. I would also like to reflect the concepts of Trust, Service and Expertise.

The website must be serious and upmarket.

Target Market(s)

Corporate board members, CFO's, treasurers and controllers
Auditors, tax advisors, private equity and venture capital asset managers, investors, tax authorities

Industry/Entity Type

Financial Service

Coding

Coded - Design and coding required

Number of Pages Required

5+ page

Font styles to use
Sans Serif
Other font styles liked:
• Designer can choose another modern font

Colors
0355a3
3277b5
85acd3
eaf1f7
f37122
f68d4d
9bcb3c
acd037
cadf82

Requirements
Must have
• Good hi resolution pictures that convey "Finance", "Trust", "Service" or "Expertise".
• An anti-bot (such as Captcha) mechanism in the contact form.
Should not have
• Must not have all content on one rolling screen.

```html
<!DOCTYPE html>
<html lang="en">
<head>
<meta charset="utf-8">
<title>Orbel Appraisals</title>
<link href="https://fonts.googleapis.com/css2?family=Montserrat:wght@500;600;700;800&family=Mulish:wght@400;600;700&display=swap" rel="stylesheet">
<style>
:root{
  --blue-dark:#0355a3;
  --blue:#3277b5;
  --blue-light:#85acd3;
  --blue-pale:#eaf1f7;
  --orange:#f37122;
  --orange-light:#f68d4d;
  --green:#9bcb3c;
  --green-mid:#acd037;
  --green-light:#cadf82;
  --ink:#222;
  --text:#666;
  --footer:#232323;
  --icon-bg:#f1f1f1;
}
*{margin:0;padding:0;box-sizing:border-box}
html,body{width:800px;height:1200px;overflow:hidden;background:#fff}
body{position:relative;font-family:"Mulish",sans-serif;color:var(--text)}
.hero{position:absolute;left:0;top:0;width:800px;height:450px;background:linear-gradient(100deg,#2f6db3 0%,#1f5fac 45%,#1a5aa8 100%);overflow:hidden}
.hero-photo{position:absolute;left:346px;top:57px;width:350px;height:350px;border-radius:50%;background:radial-gradient(circle at 55% 40%,#c9a889 0%,#8a7462 35%,#34507a 70%,#1d4a8c 100%)}
.hero-ring{position:absolute;left:358px;top:70px;width:326px;height:326px;border-radius:50%;border:2px solid rgba(255,255,255,.7)}
.brand{position:absolute;left:108px;top:34px;font-family:"Montserrat",sans-serif;font-weight:600;font-size:13px;color:#fff;letter-spacing:.5px}
.brand-mark{display:inline-block;width:10px;height:10px;background:#fff;margin-right:6px;vertical-align:-1px}
.nav{position:absolute;top:22px;left:390px;display:flex;font-family:"Montserrat",sans-serif;font-weight:600;font-size:7.5px;color:#fff}
.nav a{display:block;height:25px;line-height:25px;padding:0 13px;color:#fff;text-decoration:none}
.nav a.active{background:var(--green);padding:0 14px}
.hero-title{position:absolute;left:108px;top:138px;font-family:"Montserrat",sans-serif;font-weight:800;font-size:30px;line-height:40px;color:#fff;letter-spacing:-.3px}
.btn{position:absolute;left:108px;top:317px;width:110px;height:30px;background:var(--orange);color:#fff;font-family:"Montserrat",sans-serif;font-weight:700;font-size:7.5px;line-height:30px;text-align:center}
.values{position:absolute;left:108px;top:390px;display:flex;align-items:flex-start;box-shadow:0 12px 20px rgba(0,0,0,.08)}
.value{width:155px;background:linear-gradient(180deg,#fff,#f4f4f4);padding:24px 16px 0}
.value h3{font-family:"Montserrat",sans-serif;font-weight:700;font-size:15px;margin-bottom:14px}
.value p{font-size:7.5px;line-height:13px;color:var(--text)}
.value-trust{height:180px;border-top:2px solid var(--blue-light)}
.value-trust h3,.value-trust b{color:var(--blue-dark)}
.value-service{height:160px;margin-top:10px;border-top:2px solid var(--orange-light);padding-top:14px}
.value-service h3,.value-service b{color:var(--orange)}
.value-expertise{height:160px;margin-top:10px;border-top:2px solid var(--green-light);padding-top:14px}
.value-expertise h3,.value-expertise b{color:var(--green)}
.value b{font-weight:700}
.services-title{position:absolute;left:0;width:800px;top:640px;text-align:center;font-family:"Montserrat",sans-serif;font-weight:700;font-size:24px;color:var(--ink);letter-spacing:-.5px}
.service{position:absolute;width:180px;text-align:center;padding-top:20px}
.service.featured{background:#fff;box-shadow:0 0 8px rgba(0,0,0,.1);height:165px}
.service .icon{width:55px;height:55px;border-radius:50%;background:var(--icon-bg);margin:0 auto 18px;display:flex;align-items:center;justify-content:center}
.service h4{font-family:"Montserrat",sans-serif;font-weight:600;font-size:10px;color:var(--ink);margin-bottom:5px}
.service p{font-size:7.5px;line-height:13px}
.footer{position:absolute;left:0;top:1075px;width:800px;height:125px;background:var(--footer);color:#aaa;font-size:7px}
.fcol{position:absolute;top:31px}
.fcol h5{font-family:"Montserrat",sans-serif;font-weight:700;font-size:8.5px;color:var(--orange);margin-bottom:9px}
.fcol p{line-height:15px}
.fcol .hl{color:var(--green)}
.fcol .wh{color:#ddd}
.frow{display:flex;gap:6px;line-height:11px;margin-bottom:9px}
.frow.phone{color:#eee;font-size:7.5px;font-weight:600}
.badge{position:absolute;background:#4a4a4a;border-radius:4px}
</style>
</head>
<body>
<header class="hero">
  <div class="hero-photo" role="img" aria-label="Photo of two smiling business colleagues at a desk"></div>
  <div class="hero-ring"></div>
  <div class="brand"><span class="brand-mark"></span>ORBEL APPRAISALS</div>
  <nav class="nav">
    <a class="active">HOME</a><a>ABOUT</a><a>SERVICES</a><a>NEWS &amp; VIEWS</a><a>CONTACT</a>
  </nav>
  <h1 class="hero-title">BUSINESS &amp;<br>INTELLECTUAL<br>PROPERTY<br>VALUATIONS</h1>
  <div class="btn">CONTACT US TODAY</div>
</header>

<section class="values">
  <div class="value value-trust">
    <h3>TRUST</h3>
    <p><b>Trust</b> is paramount. Clients rely on Orbel Appraisals for confidentiality, transparency and independence.</p>
  </div>
  <div class="value value-service">
    <h3>SERVICES</h3>
    <p><b>Service</b> is front and center at Orbel Appraisals. We consider the needs of all stakeholders and the personal needs of the client team involved.</p>
  </div>
  <div class="value value-expertise">
    <h3>SERVICES</h3>
    <p><b>Expertise</b> is core to the philosophy of Orbel Appraisals. Our global network of professionals maintain and continue to develop the knowledge and experience that you expect from your trusted corporate finance partner.</p>
  </div>
</section>

<h2 class="services-title">OUR SERVICES</h2>

<div class="service" style="left:106px;top:687px">
  <div class="icon"><svg width="28" height="26" viewBox="0 0 28 26" fill="none" stroke="#0355a3" stroke-width="1.2"><path d="M2 2v22h24"/><path d="M6 22v-6h3v6M12 22v-9h3v9M18 22v-12h3v12"/><path d="M5 11l6-6M8 5h3v3"/></svg></div>
  <h4>Business Valuation</h4>
  <p>Company stakeholders trust Orbel Appraisals to provide business valuations for transaction, accounting, tax, legal, and...</p>
</div>
<div class="service featured" style="left:310px;top:687px">
  <div class="icon"><svg width="28" height="30" viewBox="0 0 28 30" fill="none" stroke="#f37122" stroke-width="1.2"><path d="M10 29V8h8v21M14 8V3M12 3h4M4 29V17h6M18 20h6v9M2 29h24"/><path d="M12 11h4M12 14h4M12 17h4M12 20h4M6 20h2M6 23h2M20 23h2"/></svg></div>
  <h4>Intellectual Property Valuation</h4>
  <p>Patents, unpatented technologies, know how, brands, trademarks, databases, customer-related assets - this is a limited...</p>
</div>
<div class="service" style="left:512px;top:687px">
  <div class="icon"><svg width="30" height="26" viewBox="0 0 30 26" fill="none" stroke="#9bcb3c" stroke-width="1.2"><circle cx="8" cy="4" r="2.5"/><circle cx="15" cy="4" r="2.5"/><circle cx="22" cy="4" r="2.5"/><path d="M3 12h24v4H3zM6 16v8M24 16v8M11 16v8M19 16v8M3 12c0-3 2-5 5-5M27 12c0-3-2-5-5-5"/></svg></div>
  <h4>M&amp;A Advisory</h4>
  <p>Through our international network of M&amp;A professionals, Orbel Appraisals can assist companies with buying other companies...</p>
</div>
<div class="service" style="left:209px;top:867px">
  <div class="icon"><svg width="36" height="28" viewBox="0 0 36 28" fill="none" stroke="#3277b5" stroke-width="1.2"><path d="M22 20H3V3h28v9M10 25h10M15 20v5"/><path d="M7 15l5-5 4 3 6-6"/><circle cx="28" cy="19" r="4"/><path d="M31 22l3 3"/></svg></div>
  <h4>Business Valuation</h4>
  <p>Company stakeholders trust Orbel Appraisals to provide business valuations for transaction, accounting, tax, legal, and...</p>
</div>
<div class="service" style="left:412px;top:867px">
  <div class="icon"><svg width="30" height="28" viewBox="0 0 30 28" fill="none" stroke="#9bcb3c" stroke-width="1.2"><path d="M16 26H3V2h16v6"/><path d="M6 14h7M6 18h7M6 22h8"/><circle cx="21" cy="15" r="7"/><path d="M23 12h-3a1.5 1.5 0 0 0 0 3h2a1.5 1.5 0 0 1 0 3h-3M21 10v10"/></svg></div>
  <h4>Intellectual Property Valuation</h4>
  <p>Patents, unpatented technologies, know how, brands, trademarks, databases, customer-related assets - this is a limited...</p>
</div>

<footer class="footer">
  <div class="fcol" style="left:109px">
    <h5>CREDITS</h5>
    <p>© 2019 <span class="hl">Orbel Appraisals</span></p>
    <p>Logo by <span class="wh">Mara Linden</span></p>
    <p>Website by <span class="hl">Northgate Webworks</span></p>
  </div>
  <div class="fcol" style="left:260px">
    <h5>LEIDEN</h5>
    <div class="frow"><svg width="7" height="9" viewBox="0 0 7 9"><path d="M3.5 0A3.5 3.5 0 0 0 0 3.5C0 6 3.5 9 3.5 9S7 6 7 3.5A3.5 3.5 0 0 0 3.5 0z" fill="#9bcb3c"/><circle cx="3.5" cy="3.5" r="1.2" fill="#232323"/></svg><span>Havenkade 14<br>2311 AB Leiden</span></div>
    <div class="frow phone"><svg width="8" height="8" viewBox="0 0 8 8"><path d="M1 0l2 2-1 1.2c.6 1.3 1.5 2.2 2.8 2.8L6 5l2 2-1 1C3.5 8 0 4.5 0 1z" fill="#9bcb3c"/></svg><span>070 555 0142</span></div>
  </div>
  <div class="fcol" style="left:412px">
    <h5>AMSTERDAM</h5>
    <div class="frow"><svg width="7" height="9" viewBox="0 0 7 9"><path d="M3.5 0A3.5 3.5 0 0 0 0 3.5C0 6 3.5 9 3.5 9S7 6 7 3.5A3.5 3.5 0 0 0 3.5 0z" fill="#9bcb3c"/><circle cx="3.5" cy="3.5" r="1.2" fill="#232323"/></svg><span>Keizerslaan 8<br>1011 AA Amsterdam</span></div>
    <div class="frow phone"><svg width="8" height="8" viewBox="0 0 8 8"><path d="M1 0l2 2-1 1.2c.6 1.3 1.5 2.2 2.8 2.8L6 5l2 2-1 1C3.5 8 0 4.5 0 1z" fill="#9bcb3c"/></svg><span>020 555 0187</span></div>
  </div>
  <div class="badge" style="left:570px;top:22px;width:114px;height:26px"></div>
  <div class="badge" style="left:570px;top:60px;width:114px;height:44px"></div>
</footer>
</body>
</html>
```